Letterhead and Envelope Design for Investment Company

We need a letterhead and envelope design.
We are a family owned investment company doing direct investments into other family owned businesses.
I have attached all our current marketing material including our logo for reference.

Our under construction website can be found here:
https://owen-darby-qk7m.sitebrella.example/
password: Marrowdale

Target Market(s)

Bankers, business owners, financial partners

Industry/Entity Type

Investment

Colors

Designer to choose colors to be used in the design.

Requirements
Must have
• Logo, and company information

```html
<!DOCTYPE html>
<html lang="en">
<head>
<meta charset="utf-8">
<title>Marrowdale Holdings Stationery</title>
<link href="https://fonts.googleapis.com/css2?family=Didact+Gothic&display=swap" rel="stylesheet">
<style>
  :root{
    --backdrop:#d4d4d4;
    --paper:#f2f2f2;
    --charcoal:#3a3a3a;
    --gold:#c9962f;
    --ink:#333333;
    --white:#ffffff;
  }
  *{margin:0;padding:0;box-sizing:border-box}
  html,body{width:1200px;height:1051px;overflow:hidden}
  body{background:var(--backdrop);font-family:"Didact Gothic",sans-serif;color:var(--ink);position:relative}
  .sheet{position:absolute;background:var(--paper);overflow:hidden}
  .sheet svg{position:absolute;left:0;display:block}

  /* Folder */
  .folder{left:165px;top:90px;width:418px;height:542px;border-radius:3px}
  .folder .spine{position:absolute;left:26px;top:0;width:2px;height:100%;background:rgba(0,0,0,.08)}
  .folder .brand{position:absolute;top:124px;left:0;width:100%;text-align:center;font-size:18.5px;letter-spacing:.4px;color:var(--ink);line-height:1.05;z-index:1}
  .folder .brand small{display:block;font-size:9.5px;letter-spacing:1px;margin-top:1px}
  .folder .web{position:absolute;bottom:29px;width:100%;text-align:center;color:var(--white);font-size:8px}

  /* Letterhead */
  .letterhead{left:615px;top:110px;width:403px;height:522px}
  .letterhead .brand{position:absolute;left:34px;top:58px;font-size:10.5px;color:var(--ink);line-height:1}
  .letterhead .brand small{display:block;text-align:center;font-size:5.5px;margin-top:1px}
  .contact{position:absolute;left:297px;top:31px;font-size:5.6px;line-height:7px}
  .contact li{list-style:none;display:flex;align-items:center;gap:3px}
  .contact .dot{width:5px;height:5px;background:var(--gold);display:inline-block}
  .contact .addr{margin-top:4px}
  .letter{position:absolute;left:37px;top:123px;width:331px;font-size:5.7px;line-height:7.1px}
  .letter p{text-align:justify;margin-bottom:7px}
  .letter .date{margin-bottom:9px}
  .letter .recipient{margin-bottom:29px;text-align:left}
  .letter .salute{font-weight:bold}
  .sign{display:flex;gap:12px;align-items:flex-start}
  .sign .who{font-weight:bold}
  .signature{width:80px;height:34px;background:linear-gradient(90deg,#e4e6f1,#d9ddee);border-radius:2px}
  .footer-web{position:absolute;right:42px;bottom:3px;color:var(--white);font-size:6.4px;z-index:1}

  /* Compliment slip */
  .slip{left:131px;top:660px;width:452px;height:195px}
  .slip .brand{position:absolute;left:19px;top:47px;font-size:10px;line-height:1}
  .slip .brand small{display:block;text-align:center;font-size:5.2px;margin-top:1px}
  .slip .addr{position:absolute;left:19px;top:168px;font-size:5.5px;line-height:6.8px}
  .slip .footer-web{right:33px}

  /* Envelope */
  .envelope{left:615px;top:660px;width:451px;height:195px}
  .envelope .flap-brand{position:absolute;top:28px;width:100%;text-align:center;color:var(--gold);font-size:9px;letter-spacing:.5px;z-index:1}
  .envelope .web{position:absolute;top:166px;width:100%;text-align:center;font-size:5.6px}
</style>
</head>
<body>

<section class="sheet folder" aria-label="Presentation folder">
  <span class="spine"></span>
  <div class="brand">MARROWDALE HOLDINGS<small>INC</small></div>
  <svg width="418" height="542" viewBox="0 0 418 542" style="top:0">
    <path d="M0,236 Q150,212 292,222 Q150,226 0,254 Z" fill="var(--gold)"/>
    <path d="M0,262 Q200,226 418,226 L418,542 L0,542 Z" fill="var(--charcoal)"/>
  </svg>
  <div class="web">www.marrowdaleholdings.example</div>
</section>

<section class="sheet letterhead" aria-label="Letterhead">
  <div class="brand">MARROWDALE HOLDINGS<small>INC</small></div>
  <ul class="contact">
    <li><span class="dot"></span>800.555.0142</li>
    <li><span class="dot"></span>info@LakemereCA.example</li>
    <li><span class="dot"></span>www.LakemereCA.example</li>
    <li class="addr">48 Orchard Row, FL 3</li>
    <li>Fernhaven FL 33100</li>
  </ul>
  <div class="letter">
    <p class="date">30.09.2015</p>
    <p class="recipient">Recipient's name<br>Lindenweg 4<br>10115 Berlin<br>Germany</p>
    <p class="salute">Dear sir,</p>
    <p>Communication is a very integral part of living creatures, animals and humans. Communication may be verbal or written. Written communication however is only applicable to human beings. Can you even imagine a world without communication? Verbal communication can be through telephones, webcams or in person. Written communication is through letters, emails and mobile phone messages.</p>
    <p>In today's world of great inventions and technology, letters have somehow become redundant. It is the time for text messages or chats. But they still can communicate a lot more than all other modes of communication. Organizations and various government departments still bank on letters as a strong medium of communication. There is no comparison in costs of sending letters as compared to costs of mobile phone messages though – letters are far cheaper. Letters now commonly known as "hard copy documents" are considered more relevant and important than email copies of text messages as proof or evidence of some sort.</p>
    <p>Letters speak volumes about a person or an organization that writes it. So one must take utmost care ensuring that the language used in any letter is appropriate for the occasion for which it is being written. Since a letter is also a written proof or document, if there are certain things that should not form a part of it, then that too should be carefully handled.</p>
    <p>Writing a good letter is an art. But if for some reason someone is unable to write that perfect letter, these different types of letters provide a base for you to build on. Sample letters have been given for everyone to understand what all information needs to form a part of the letter type and then it can be customized.</p>
    <div class="sign">
      <div>Yours Sincerely,<br><span class="who">Lena Hartwell</span></div>
      <div class="signature" role="img" aria-label="Handwritten signature"></div>
    </div>
  </div>
  <svg width="403" height="22" viewBox="0 0 403 22" style="bottom:0">
    <path d="M104,22 Q210,4 322,2 Q220,8 130,22 Z" fill="var(--gold)"/>
    <path d="M150,22 Q260,5 403,5 L403,22 Z" fill="var(--charcoal)"/>
  </svg>
  <div class="footer-web">www.<b>LakemereCA</b>.example</div>
</section>

<section class="sheet slip" aria-label="Compliment slip">
  <div class="brand">MARROWDALE HOLDINGS<small>INC</small></div>
  <div class="addr">310 Elm Ave. NE; Suite 200<br>Brookvale, IA 50000</div>
  <svg width="452" height="24" viewBox="0 0 452 24" style="bottom:0">
    <path d="M155,24 Q265,6 380,3 Q275,10 185,24 Z" fill="var(--gold)"/>
    <path d="M205,24 Q320,6 452,7 L452,24 Z" fill="var(--charcoal)"/>
  </svg>
  <div class="footer-web">www.<b>LakemereCA</b>.example</div>
</section>

<section class="sheet envelope" aria-label="Envelope">
  <svg width="451" height="64" viewBox="0 0 451 64" style="top:0">
    <path d="M0,0 L451,0 L432,62 L19,62 Z" fill="var(--charcoal)"/>
  </svg>
  <div class="flap-brand">MARROWDALE</div>
  <div class="web">www.LakemereCA.example</div>
</section>

</body>
</html>
```